Page lark & Glimmerly ad needed

I am in need of a simple static image ad to be used for Pagelark & Glimmerly. A photo of a nice roof on a nice house. "Instant Satellite Roof Estimates" "Your house, your time & instant estimate" . Our logo file is here: https://www.filquarry.com/scl/fo/t52wqpzx73hmbnvekcy8d/ZKqWT5PLmNdbX3HfGsYe8r2?rlkey=vn7cz2ktbw94pqdr6yjmfx4cs&dl=0

Multiple variations will be purchased.

```html
<!DOCTYPE html>
<html lang="en">
<head>
<meta charset="utf-8">
<title>Crestwell Roofing — Ad Set</title>
<link href="https://fonts.googleapis.com/css2?family=Barlow+Condensed:wght@600;700&family=Montserrat:wght@500&display=swap" rel="stylesheet">
<style>
  :root{
    --page:#ffffff;
    --ink:#111111;
    --navy:#03023a;
    --card-white:#fdfcfa;
    --sky-top:#5e9fd6;
    --sky-low:#a9cdee;
    --roof:#3f4449;
    --roof-dark:#2a2e33;
    --wall:#e9e6e0;
    --teal:#3f6670;
    --teal-light:#6f9098;
    --head:"Barlow Condensed", sans-serif;
    --body:"Montserrat", sans-serif;
  }
  *{box-sizing:border-box;margin:0;padding:0}
  html,body{width:1200px;height:1200px;overflow:hidden;background:var(--page)}
  .canvas{position:relative;width:1200px;height:1200px}
  .ad{position:absolute;width:338px;height:422px;overflow:hidden}
  .ad--video{height:600px}
  .photo{position:absolute;inset:0}
  .photo--house{background:linear-gradient(180deg,var(--sky-top) 0%,var(--sky-low) 42%,var(--roof) 60%,var(--roof-dark) 78%,var(--wall) 100%)}
  .photo--house-low{background:linear-gradient(180deg,var(--sky-top) 0%,var(--sky-low) 30%,var(--roof) 48%,var(--roof-dark) 70%,var(--wall) 100%)}
  .photo--tiles{background:linear-gradient(160deg,var(--teal-light) 0%,var(--teal) 55%,#34575f 100%)}
  .brand{font-family:var(--head);font-weight:600;letter-spacing:.04em;text-transform:uppercase;line-height:1}
  .top-copy{position:absolute;left:0;right:0;top:34px;text-align:center;color:var(--ink)}
  .top-copy .brand{font-size:20px}
  .headline{font-family:var(--head);font-weight:700;line-height:.92;letter-spacing:.005em}
  .top-copy .headline{font-size:39px;margin-top:42px}
  .top-copy .sub{font-family:var(--head);font-weight:600;font-size:17px;margin-top:6px}
  .card{position:absolute;border-radius:16px;padding:20px 22px}
  .card--navy{background:var(--navy);color:#fff}
  .card--white{background:var(--card-white);color:var(--ink)}
  .card--tall{left:78px;top:122px;width:183px;height:279px}
  .card--tall .brand{text-align:center;font-size:13px}
  .card--tall .headline{font-size:34px;margin-top:34px}
  .card .sub{font-family:var(--body);font-weight:500;font-size:12px;line-height:1.1;margin-top:14px}
  .card--wide{left:36px;top:182px;width:266px;height:240px;border-radius:16px 16px 0 0;padding:20px 26px}
  .card--wide .brand{text-align:center;font-size:18px}
  .card--wide .headline{font-size:37px;margin-top:28px}
  .card--wide .sub{font-size:15.5px;margin-top:8px}
  .ad--video .brand{position:absolute;left:0;right:0;top:120px;text-align:center;color:#fff;font-size:24px}
  .offer{position:absolute;left:403px;top:1022px;transform:translateX(-50%);text-align:center;font-family:var(--head);font-weight:700;font-size:66px;line-height:.95;color:var(--ink);white-space:nowrap}
</style>
</head>
<body>
<main class="canvas">

  <section class="ad" style="left:39px;top:59px">
    <div class="photo photo--house" role="img" aria-label="Modern house with dark grey tiled hip roof under a clear blue sky"></div>
    <div class="top-copy">
      <p class="brand">Crestwell Roofing</p>
      <h2 class="headline">Instant Satellite<br>Roof Estimates</h2>
      <p class="sub">Your house, your time &amp; instant estimate</p>
    </div>
  </section>

  <section class="ad" style="left:431px;top:59px">
    <div class="photo photo--house" role="img" aria-label="Front of a house with a grey tiled roof against blue sky"></div>
    <div class="top-copy">
      <p class="brand">Crestwell Roofing</p>
      <h2 class="headline">Instant Satellite<br>Roof Estimates</h2>
      <p class="sub">Your house, your time &amp; instant estimate</p>
    </div>
  </section>

  <section class="ad" style="left:823px;top:59px">
    <div class="photo photo--house-low" role="img" aria-label="House with dark tiled roof, stone and timber walls, blue sky"></div>
    <div class="card card--navy card--tall">
      <p class="brand">Crestwell Roofing</p>
      <h2 class="headline">Instant<br>Satellite<br>Roof<br>Estimates</h2>
      <p class="sub">Your house, your time<br>&amp; instant estimate</p>
    </div>
  </section>

  <section class="ad" style="left:39px;top:541px">
    <div class="photo photo--house-low" role="img" aria-label="House with dark tiled roof, stone and timber walls, blue sky"></div>
    <div class="card card--white card--tall">
      <p class="brand">Crestwell Roofing</p>
      <h2 class="headline">Instant<br>Satellite<br>Roof<br>Estimates</h2>
      <p class="sub">Your house, your time<br>&amp; instant estimate</p>
    </div>
  </section>

  <section class="ad" style="left:431px;top:541px">
    <div class="photo photo--house-low" role="img" aria-label="Grey tiled hip roof of a modern house under blue sky"></div>
    <div class="card card--navy card--wide">
      <p class="brand">Crestwell Roofing</p>
      <h2 class="headline">Instant<br>Satellite Roof<br>Estimates</h2>
      <p class="sub">Your house, your time<br>&amp; instant estimate</p>
    </div>
  </section>

  <section class="ad ad--video" style="left:823px;top:541px">
    <div class="photo photo--tiles" role="img" aria-label="Aerial close-up of a teal-grey metal tile roof with ridge lines and a skylight"></div>
    <p class="brand">Crestwell Roofing</p>
  </section>

  <p class="offer">5 Ads Design<br>Free 1 Ads Video</p>

</main>
</body>
</html>
```